International wholesale business needs a business card

We need a business card.

Company Details:
Company Name and logo
Address, Phone number, Website
Employee Details:
Name, Designation, Mobile Number & Email address

Logo file is attached.

```html
<!DOCTYPE html>
<html lang="en">
<head>
<meta charset="utf-8">
<title>Corvane Trading — Business Card</title>
<link rel="stylesheet" href="https://fonts.googleapis.com/css2?family=Lato:wght@400;700&family=Oswald:wght@500&display=swap">
<style>
  :root {
    --backdrop: #1c1c1e;
    --card: #111112;
    --accent: #c8242d;
    --text-light: #f2f2f2;
    --divider: #8a8a8a;
  }
  * { box-sizing: border-box; margin: 0; padding: 0; }
  html, body {
    width: 1200px;
    height: 900px;
    overflow: hidden;
    background: var(--backdrop);
  }
  .canvas {
    width: 1200px;
    height: 900px;
    display: flex;
    flex-direction: column;
    align-items: center;
    justify-content: center;
    gap: 44px;
  }
  .card {
    position: relative;
    width: 640px;
    height: 366px;
    background: var(--card);
    box-shadow: 0 10px 30px rgba(0,0,0,0.55);
    overflow: hidden;
  }
  .card__band {
    position: absolute;
    left: 0; right: 0; bottom: 0;
    height: 12px;
    background: var(--accent);
  }

  /* Front */
  .brand {
    position: absolute;
    top: 110px;
    left: 0; right: 0;
    display: flex;
    align-items: center;
    justify-content: center;
    gap: 16px;
  }
  .brand__mark {
    width: 46px;
    height: 46px;
    border-radius: 50%;
    background: var(--accent);
  }
  .brand__name {
    font-family: "Lato", sans-serif;
    font-weight: 700;
    font-size: 44px;
    letter-spacing: 3px;
    text-transform: uppercase;
    color: var(--accent);
  }
  .front__web {
    position: absolute;
    left: 0; right: 0;
    bottom: 52px;
    text-align: center;
    font-family: "Lato", sans-serif;
    font-size: 17px;
    letter-spacing: 1.5px;
    color: var(--text-light);
  }

  /* Back */
  .person {
    position: absolute;
    top: 118px;
    left: 80px;
    width: 230px;
    text-align: right;
  }
  .person__name {
    font-family: "Oswald", sans-serif;
    font-weight: 500;
    font-size: 36px;
    line-height: 1;
    text-transform: uppercase;
    color: var(--accent);
  }
  .person__role {
    margin-top: 6px;
    font-family: "Lato", sans-serif;
    font-size: 17px;
    letter-spacing: 0.5px;
    color: var(--text-light);
  }
  .back__divider {
    position: absolute;
    top: 112px;
    left: 334px;
    width: 1px;
    height: 92px;
    background: var(--divider);
  }
  .contacts {
    position: absolute;
    top: 118px;
    left: 356px;
    list-style: none;
    font-family: "Lato", sans-serif;
    font-size: 17px;
    color: var(--text-light);
  }
  .contacts__item {
    display: flex;
    align-items: center;
    gap: 10px;
    height: 27px;
  }
  .contacts__icon {
    width: 16px;
    height: 16px;
    flex: none;
  }
  .back__address {
    position: absolute;
    left: 0; right: 0;
    bottom: 44px;
    text-align: center;
    font-family: "Lato", sans-serif;
    font-size: 18px;
    letter-spacing: 0.5px;
    color: var(--text-light);
  }
</style>
</head>
<body>
<main class="canvas">
  <section class="card card--front">
    <div class="brand">
      <span class="brand__mark"></span>
      <span class="brand__name">Corvane Trading</span>
    </div>
    <p class="front__web">www.corvanetrading.com</p>
    <div class="card__band"></div>
  </section>

  <section class="card card--back">
    <div class="person">
      <h1 class="person__name">Daniel Reyes</h1>
      <p class="person__role">Managing Director</p>
    </div>
    <div class="back__divider"></div>
    <ul class="contacts">
      <li class="contacts__item">
        <svg class="contacts__icon" viewBox="0 0 24 24" aria-hidden="true">
          <path fill="#c8242d" d="M6.6 10.8a15.1 15.1 0 0 0 6.6 6.6l2.2-2.2a1 1 0 0 1 1-.25 11.4 11.4 0 0 0 3.6.57 1 1 0 0 1 1 1V20a1 1 0 0 1-1 1A17 17 0 0 1 3 4a1 1 0 0 1 1-1h3.5a1 1 0 0 1 1 1c0 1.25.2 2.45.57 3.57a1 1 0 0 1-.25 1z"/>
        </svg>
        <span>041-555 302 118</span>
      </li>
      <li class="contacts__item">
        <svg class="contacts__icon" viewBox="0 0 24 24" aria-hidden="true">
          <rect x="2" y="5" width="20" height="14" fill="#c8242d"/>
          <path d="M2 5l10 8 10-8" fill="none" stroke="#111112" stroke-width="1.8"/>
        </svg>
        <span>hello@corvanetrading.com</span>
      </li>
      <li class="contacts__item">
        <svg class="contacts__icon" viewBox="0 0 24 24" aria-hidden="true">
          <g fill="none" stroke="#c8242d" stroke-width="2">
            <circle cx="12" cy="12" r="9.5"/>
            <ellipse cx="12" cy="12" rx="4" ry="9.5"/>
            <path d="M2.5 12h19M4 7h16M4 17h16"/>
          </g>
        </svg>
        <span>www.corvanetrading.com</span>
      </li>
    </ul>
    <p class="back__address">17 Harbour Road, Portvale, 30218</p>
    <div class="card__band"></div>
  </section>
</main>
</body>
</html>
```